Business Card Design Project 4 Construction Business

I am after a creative, but sleek and simple/ clean business card design. This design will form the basis of future items and might include a logo or simply a creative way to lay out the text of my company name 'kestrel ventures'
I like the simplicity of black and white however I would also be happy to see a splash of colour introduced somehow to give the text some interest and make it stand out.
I would like a double sided card.
I am young (ish!) and professional, offering construction and project management services, what I don't want is the traditional builders type card featuring a cheesy hammer/ saw image etc.
As the company name, kestrel ventures, suggests, we focus on working closely and collaboratively together, in synergy with all stakeholders involved in the projects that we undertake
Construction

```html
<!DOCTYPE html>
<html lang="en">
<head>
<meta charset="utf-8">
<title>Kestrel Ventures – Business Card</title>
<link rel="stylesheet" href="https://fonts.googleapis.com/css2?family=Montserrat:wght@500;600&family=Questrial&display=swap">
<style>
  :root {
    --ink: #1b1b1b;
    --paper: #ffffff;
    --line: #3a3a3a;
    --muted: #5e5e5e;
    --grey: #8f8f8f;
  }
  * { margin: 0; padding: 0; box-sizing: border-box; }
  html, body { width: 842px; height: 1200px; overflow: hidden; background: var(--paper); }
  .sheet { position: relative; width: 842px; height: 1200px; }

  .card { position: absolute; left: 0; width: 841px; height: 504px; border-radius: 32px; overflow: hidden; }
  .card--front { top: 0; background: var(--paper); border: 1px solid var(--line); }
  .card--back { top: 694px; background: var(--ink); }

  .brand-block { position: absolute; left: 397px; top: 0; width: 385px; height: 160px; background: var(--ink); }
  .wordmark { position: absolute; font-family: "Montserrat", sans-serif; font-weight: 600; text-transform: uppercase; line-height: 1; white-space: nowrap; }
  .wordmark__main { display: block; letter-spacing: 0.04em; }
  .wordmark__sub { display: block; letter-spacing: 0.42em; }

  .card--front .wordmark { left: 408px; top: 172px; color: var(--ink); }
  .card--front .wordmark__main { font-size: 40px; }
  .card--front .wordmark__sub { font-size: 25px; margin-top: 14px; }

  .holder { position: absolute; left: 46px; top: 328px; }
  .holder__name { font-family: "Montserrat", sans-serif; font-weight: 500; font-size: 25px; color: #111; letter-spacing: 0.02em; }
  .holder__role { font-family: "Questrial", sans-serif; font-size: 19px; color: var(--muted); margin-top: 16px; }

  .contact { position: absolute; left: 398px; top: 325px; list-style: none; font-family: "Questrial", sans-serif; font-size: 16.5px; color: #333; }
  .contact li { height: 46.5px; white-space: nowrap; }
  .contact__label { margin-right: 4px; }

  .card--back .wordmark { left: 0; right: 0; top: 146px; text-align: center; color: var(--grey); }
  .card--back .wordmark__main { font-size: 46px; }
  .card--back .wordmark__sub { font-size: 31px; margin-top: 22px; padding-left: 0.42em; }

  .website { position: absolute; left: 0; right: 0; top: 288px; text-align: center; font-family: "Questrial", sans-serif; font-size: 26px; letter-spacing: 0.04em; color: var(--grey); }
</style>
</head>
<body>
<main class="sheet">
  <section class="card card--front" aria-label="Card front">
    <div class="brand-block"></div>
    <div class="wordmark">
      <span class="wordmark__main">Kestrel</span>
      <span class="wordmark__sub">Ventures</span>
    </div>
    <div class="holder">
      <p class="holder__name">LIAM CARVER</p>
      <p class="holder__role">Director</p>
    </div>
    <ul class="contact">
      <li><span class="contact__label">P :</span>0400 555 123</li>
      <li><span class="contact__label">E :</span>liam@kestrelventuresgroup.com.au</li>
      <li><span class="contact__label">A :</span>14 Harbour Ln Northbridge NSW 2063</li>
    </ul>
  </section>

  <section class="card card--back" aria-label="Card back">
    <div class="wordmark">
      <span class="wordmark__main">Kestrel</span>
      <span class="wordmark__sub">Ventures</span>
    </div>
    <p class="website">www.kestrelventuresgroup.com.au</p>
  </section>
</main>
</body>
</html>
```